Higher co-efficient of performance means more heat for your money

I need a bar graph that will have the following heating systems, 80% efficient gas furnace COP of .8, Electric heat COP of 1, and Our best selling heat pump with a cop of 4 at 47F. I will have a constant bar, 100$ worth of gas for furnace, 100$ of electricity for electric heat, and 100$ worth of electricity for our heat pumps. next to them I will have a bar showing how much heat each heating system will provide for $100 of fuel. For gas furnace I need a bar that says $80 worth of heat and the barograph to match it, for electric heat I need the bar to show 100$ worth of heat, for our best selling heat pump I need the bar graph to show and say $400 dollars worth of heat. Please take a look at my website www.summitbreezecomfort.example for brand color and feel

```html
<!DOCTYPE html>
<html lang="en">
<head>
<meta charset="utf-8">
<title>More Heat For Your Money – Summit Breeze Comfort</title>
<link rel="stylesheet" href="https://fonts.googleapis.com/css2?family=Audiowide&family=Montserrat:wght@400;700&display=swap">
<style>
  :root {
    --brand-blue: #0a6bb8;
    --brand-red: #c1272d;
    --ink: #1b1b1b;
    --rule: #c9c9c9;
    --faint-blue: #eef4fa;
    --paper: #ffffff;
  }
  html, body {
    margin: 0;
    padding: 0;
    overflow: hidden;
    background: var(--paper);
  }
  .canvas {
    position: relative;
    width: 965px;
    height: 1200px;
    overflow: hidden;
    background: var(--paper);
  }
  .brand {
    position: absolute;
    left: 100px;
    top: 138px;
    width: 205px;
    text-align: center;
    color: var(--brand-blue);
    font-family: "Audiowide", sans-serif;
    font-size: 21px;
    line-height: 1.15;
  }
  .brand-dot {
    display: block;
    width: 46px;
    height: 46px;
    margin: 0 auto 12px;
    border-radius: 50%;
    background: var(--brand-blue);
  }
  .header-divider {
    position: absolute;
    left: 316px;
    top: 133px;
    width: 3px;
    height: 128px;
    background: var(--brand-red);
  }
  .headline {
    position: absolute;
    left: 343px;
    top: 126px;
    margin: 0;
    font-family: "Audiowide", sans-serif;
    font-weight: 400;
    white-space: nowrap;
  }
  .headline-kicker {
    display: block;
    color: var(--brand-blue);
    font-size: 19.5px;
    letter-spacing: 1.2px;
  }
  .headline-main {
    display: block;
    color: var(--brand-red);
    font-size: 43px;
    line-height: 47px;
    letter-spacing: 1.6px;
    margin-top: 2px;
  }
  .footnote {
    position: absolute;
    left: 342px;
    top: 245px;
    margin: 0;
    color: var(--brand-blue);
    font-family: "Montserrat", sans-serif;
    font-size: 15.5px;
  }
  .chart {
    position: absolute;
    left: 0;
    top: 0;
  }
  .watermark {
    font-family: "Audiowide", sans-serif;
    font-size: 84px;
    fill: var(--faint-blue);
  }
  .value-blue { font-family: "Montserrat", sans-serif; font-weight: 700; font-size: 41px; fill: var(--brand-blue); }
  .value-red  { font-family: "Montserrat", sans-serif; font-weight: 700; font-size: 41px; fill: var(--brand-red); }
  .value-tag  { font-family: "Montserrat", sans-serif; font-weight: 700; font-size: 56px; fill: #fff; }
  .bar-caption { font-family: "Montserrat", sans-serif; font-size: 15px; fill: #fff; letter-spacing: 0.5px; }
  .bar-caption-small { font-size: 12.5px; }
  .bar-caption-large { font-size: 30px; }
  .system-label { font-family: "Audiowide", sans-serif; font-size: 23px; fill: var(--ink); letter-spacing: 1px; }
  .system-label-blue { fill: var(--brand-blue); }
  .system-label-red { font-size: 34px; fill: var(--brand-red); }
</style>
</head>
<body>
<main class="canvas">
  <div class="brand"><span class="brand-dot"></span>SUMMIT BREEZE<br>COMFORT</div>
  <div class="header-divider"></div>
  <h1 class="headline">
    <span class="headline-kicker">HIGHER CO-EFFICIENT OF PERFORMANCE</span>
    <span class="headline-main">MEANS MORE HEAT<br>FOR YOUR MONEY</span>
  </h1>
  <p class="footnote">*COP measure at 47°F</p>

  <svg class="chart" width="965" height="1200" viewBox="0 0 965 1200" role="img" aria-label="Bar chart: $100 of energy gives $80 of heat from an 80% gas furnace, $100 from electric heat, and $400 from the heat pump">
    <defs>
      <linearGradient id="blue-body" x1="0" x2="1" y1="0" y2="0">
        <stop offset="0" stop-color="#0a4f8f"/>
        <stop offset="0.45" stop-color="#1778c4"/>
        <stop offset="1" stop-color="#0a5598"/>
      </linearGradient>
      <linearGradient id="red-body" x1="0" x2="1" y1="0" y2="0">
        <stop offset="0" stop-color="#8a1217"/>
        <stop offset="0.5" stop-color="#c1272d"/>
        <stop offset="1" stop-color="#a11b21"/>
      </linearGradient>
      <linearGradient id="blue-top" x1="0" x2="1">
        <stop offset="0" stop-color="#0d5da3"/>
        <stop offset="1" stop-color="#2a88d0"/>
      </linearGradient>
      <linearGradient id="red-top" x1="0" x2="1">
        <stop offset="0" stop-color="#a91d23"/>
        <stop offset="1" stop-color="#d63a40"/>
      </linearGradient>
    </defs>

    <text class="watermark" x="470" y="705" text-anchor="middle">SUMMIT BREEZE</text>

    <line x1="28" y1="982" x2="941" y2="982" stroke="var(--rule)" stroke-width="1.5"/>

    <!-- Gas furnace -->
    <g class="bar-group">
      <path d="M95 801 L95 985 A37 11 0 0 0 169 985 L169 801 Z" fill="url(#blue-body)"/>
      <ellipse cx="132" cy="801" rx="37" ry="11" fill="url(#blue-top)"/>
      <text class="bar-caption" transform="translate(132 842) rotate(90)" dominant-baseline="middle">OF ELECTRICITY</text>
      <text class="value-blue" x="127" y="776" text-anchor="middle">$100</text>

      <path d="M204 835 L204 985 A37 11 0 0 0 278 985 L278 835 Z" fill="url(#red-body)"/>
      <ellipse cx="241" cy="835" rx="37" ry="11" fill="url(#red-top)"/>
      <text class="bar-caption bar-caption-small" transform="translate(241 858) rotate(90)" dominant-baseline="middle">WORTH OF HEAT</text>
      <text class="value-red" x="236" y="810" text-anchor="middle">$80</text>

      <text class="system-label" x="185" y="1044" text-anchor="middle">80%</text>
      <text class="system-label" x="185" y="1071" text-anchor="middle">GAS FURNACE</text>
    </g>

    <!-- Electric heat -->
    <g class="bar-group">
      <path d="M371 801 L371 985 A37 11 0 0 0 445 985 L445 801 Z" fill="url(#blue-body)"/>
      <ellipse cx="408" cy="801" rx="37" ry="11" fill="url(#blue-top)"/>
      <text class="bar-caption" transform="translate(408 842) rotate(90)" dominant-baseline="middle">OF ELECTRICITY</text>
      <text class="value-blue" x="402" y="776" text-anchor="middle">$100</text>

      <path d="M481 801 L481 985 A37 11 0 0 0 555 985 L555 801 Z" fill="url(#red-body)"/>
      <ellipse cx="518" cy="801" rx="37" ry="11" fill="url(#red-top)"/>
      <text class="bar-caption" transform="translate(518 826) rotate(90)" dominant-baseline="middle">WORTH OF HEAT</text>
      <text class="value-red" x="512" y="776" text-anchor="middle">$100</text>

      <text class="system-label" x="462" y="1044" text-anchor="middle">ELECTRIC</text>
      <text class="system-label" x="462" y="1071" text-anchor="middle">HEAT</text>
    </g>

    <!-- Heat pump -->
    <g class="bar-group">
      <path d="M647 801 L647 985 A37 11 0 0 0 721 985 L721 801 Z" fill="url(#blue-body)"/>
      <ellipse cx="684" cy="801" rx="37" ry="11" fill="url(#blue-top)"/>
      <text class="bar-caption" transform="translate(684 842) rotate(90)" dominant-baseline="middle">OF ELECTRICITY</text>
      <text class="value-blue" x="675" y="776" text-anchor="middle">$100</text>

      <path d="M757 328 L757 985 A37 11 0 0 0 831 985 L831 328 Z" fill="url(#red-body)"/>
      <ellipse cx="794" cy="328" rx="37" ry="13" fill="url(#red-top)"/>
      <text class="bar-caption bar-caption-large" transform="translate(794 720) rotate(90)" dominant-baseline="middle">WORTH OF HEAT</text>

      <polygon points="677,589 874,589 895,627 874,666 677,666" fill="var(--brand-red)" stroke="#ffffff" stroke-opacity="0.25" stroke-width="1"/>
      <text class="value-tag" x="775" y="647" text-anchor="middle">$400</text>

      <text class="system-label system-label-blue" x="740" y="1044" text-anchor="middle">OUR BEST SELLING</text>
      <text class="system-label system-label-red" x="740" y="1081" text-anchor="middle">HEAT PUMP</text>
    </g>
  </svg>
</main>
</body>
</html>
```